Brightmoor Capital Partners- Business Card

We need a professional business card that conveys confidence and trust. Strength. A modern and still yet, traditional financial planner/advisor format. I will upload a logo file or two, you do not have to use it, if it does not work for the design.

Target Market(s)

high net worth

Industry/Entity Type

Finance

Contact Information for Business Card

Address: 24853 Harlow Ave. Suite 610, Huntington Beach, CA 90318, website: brightmoorcapital.example, ph # (555) 276-1948, email address: mpellegrin@brightmoorcapital.example

```html
<!DOCTYPE html>
<html lang="en">
<head>
<meta charset="utf-8">
<title>Brightmoor Capital Partners – Business Card</title>
<link rel="stylesheet" href="https://fonts.googleapis.com/css2?family=Arimo:wght@400;700&display=swap">
<style>
  :root {
    --backdrop: #e9e9e9;
    --card-white: #ffffff;
    --card-black: #1f1f22;
    --gold: #b8902e;
    --gold-edge: #a8842a;
    --ink-grey: #6e6e6e;
    --rule-grey: #9a9a9a;
  }
  * { margin: 0; padding: 0; box-sizing: border-box; }
  html, body {
    width: 1200px; height: 802px; overflow: hidden;
    background: var(--backdrop);
    font-family: "Arimo", Arial, sans-serif;
  }
  .canvas { position: relative; width: 1200px; height: 802px; }
  .card {
    position: absolute;
    width: 500px; height: 286px;
    border-bottom: 3px solid var(--gold-edge);
    box-shadow: 0 6px 18px rgba(0,0,0,0.12);
    overflow: hidden;
  }
  .card-front { left: 80px; top: 150px; background: var(--card-white); }
  .card-back  { left: 620px; top: 370px; background: var(--card-black); }

  .brand-mark {
    position: absolute;
    display: flex; align-items: center; gap: 10px;
    color: var(--gold);
    font-weight: 700;
    text-transform: uppercase;
    letter-spacing: 0.04em;
  }
  .brand-mark .mark-square { flex: none; border: 2px solid var(--gold); }
  .card-front .brand-mark {
    left: 32px; top: 118px; width: 190px;
    font-size: 14px; line-height: 1.3;
  }
  .card-front .mark-square { width: 34px; height: 34px; }

  .card-back .brand-mark {
    left: 0; right: 0; top: 0; bottom: 0;
    justify-content: center;
    font-size: 20px;
  }
  .card-back .mark-square { width: 40px; height: 40px; }

  .divider {
    position: absolute; left: 236px; top: 92px;
    width: 1px; height: 150px; background: var(--rule-grey);
  }
  .contact-block { position: absolute; left: 250px; top: 72px; right: 12px; color: var(--ink-grey); }
  .person-name {
    color: var(--gold); font-weight: 700; font-size: 17px;
    letter-spacing: 0.02em; text-transform: uppercase;
  }
  .person-title { font-size: 12px; margin-top: 2px; }
  .address { font-size: 12px; line-height: 1.35; margin-top: 14px; }
  .contact-list { list-style: none; margin-top: 12px; font-size: 12px; line-height: 1.45; }
  .contact-list li { display: flex; align-items: center; gap: 6px; white-space: nowrap; }
  .contact-list svg { width: 11px; height: 11px; flex: none; }
</style>
</head>
<body>
<main class="canvas">
  <section class="card card-front" aria-label="Business card front">
    <div class="brand-mark"><span class="mark-square"></span><span>Brightmoor Capital Partners</span></div>
    <div class="divider"></div>
    <div class="contact-block">
      <p class="person-name">Marcus Pellegrin</p>
      <p class="person-title">Manager</p>
      <p class="address">24853 Harlow Ave. Suite 610<br>Harbor Point, CA 90318</p>
      <ul class="contact-list">
        <li>
          <svg viewBox="0 0 12 12" aria-hidden="true"><path d="M3 1.5l2 2.2-1 1.2a6 6 0 0 0 3.1 3.1l1.2-1 2.2 2-1 1.5C6 10.5 1.5 6 1.5 2.5z" fill="var(--gold)"/></svg>
          <span>(555) 276-1948</span>
        </li>
        <li>
          <svg viewBox="0 0 12 12" aria-hidden="true"><rect x="1" y="2.5" width="10" height="7" fill="none" stroke="var(--gold)" stroke-width="1.2"/><path d="M1 2.5l5 4 5-4" fill="none" stroke="var(--gold)" stroke-width="1.2"/></svg>
          <span>mpellegrin@brightmoorcapital.example</span>
        </li>
        <li>
          <svg viewBox="0 0 12 12" aria-hidden="true"><circle cx="6" cy="6" r="5" fill="none" stroke="var(--gold)" stroke-width="1.2"/><path d="M1 6h10M6 1c-2.5 3-2.5 7 0 10M6 1c2.5 3 2.5 7 0 10" fill="none" stroke="var(--gold)" stroke-width="1"/></svg>
          <span>brightmoorcapital.example</span>
        </li>
      </ul>
    </div>
  </section>

  <section class="card card-back" aria-label="Business card back">
    <div class="brand-mark"><span class="mark-square"></span><span>Brightmoor Capital Partners</span></div>
  </section>
</main>
</body>
</html>
```